Inner pages of website needed (2 pages)

Hi there,

I am in the process of designing a new website (Foundation/HTML - no CMS being used). It's to replace an existing site. The home page is fine, but I need the inner pages improved. I do have some inner pages already produced, but I'm not happy with them.

The new website home page can be found here http://codelarkspur.com/project-demo/brightfold/index.html
(this is the style concept).

The old website can be found here:
http://cv-meridianworks.com.au/

To start, I will need 2 pages designed based on the new style, but migrating the information from the old site:

Resume Services Page (http://cv-meridianworks.com.au/professional-resumes.html). On the original page you'll see a number of headings:

Career Resources Page (http://cv-meridianworks.com.au/career-advice.html)

If possible, I'd like to integrate any new ideas you may have from a design perspective.

Let me know what else you need from me.

Target Market(s)

Professionals

Industry/Entity Type

Professional Service

Number of Pages Required

2 page

Colors
3176b5
0355a3
85abd2
add136
cadf82
f68d4d
f37122
f78f20

Requirements
Must have
• Please pay particular attention to the design of the new home page and consider this as a style guide. Needs to have similar fonts, look professional and clean.
Nice to have
• Some additional functionality perhaps pictures/text interchanging.

```html
<!DOCTYPE html>
<html lang="en">
<head>
<meta charset="utf-8">
<title>Career Resources – brightfold Professional Solutions</title>
<link href="https://fonts.googleapis.com/css2?family=Open+Sans:ital,wght@0,400;0,600;0,700;1,400&display=swap" rel="stylesheet">
<style>
:root{
  --blue:#0355a3;
  --blue-mid:#3176b5;
  --blue-soft:#85abd2;
  --green:#add136;
  --green-light:#cadf82;
  --orange:#f68d4d;
  --orange-deep:#f37122;
  --text:#444;
  --heading:#333;
  --grey-band:#f2f2f2;
  --footer:#262626;
}
*{margin:0;padding:0;box-sizing:border-box}
html,body{width:1200px;height:2601px;overflow:hidden}
body{font-family:"Open Sans",Arial,sans-serif;color:var(--text);background:#fff;font-size:11.5px;line-height:20px}
.wrap{width:878px;margin:0 auto;position:relative}
section{position:relative;overflow:hidden}

/* header */
.site-header{height:106px;background:var(--blue);color:#fff}
.brand{position:absolute;left:0;top:14px}
.brand-name{font-size:44px;font-weight:400;line-height:44px;letter-spacing:1px}
.brand-tag{font-size:11px;font-weight:600;letter-spacing:.5px;border-top:1px solid #fff;margin-top:2px;padding-top:2px;line-height:14px}
.brand-sub{font-size:7.5px;line-height:10px;font-weight:600}
.top-contact{position:absolute;right:0;top:26px;font-size:11px;display:flex;gap:26px}
.top-contact span{display:flex;align-items:center;gap:7px}
.main-nav{position:absolute;right:0;top:72px;display:flex;gap:47px;font-size:11px;font-weight:600}
.main-nav a{color:#fff;text-decoration:none;padding-bottom:12px}
.main-nav a.active{border-bottom:3px solid #fff}

/* hero */
.hero{height:402px;background:linear-gradient(100deg,#3a3f46 0%,#6d737a 35%,#9ea3a8 55%,#5b6167 80%,#2f3338 100%)}
.hero h1{position:absolute;left:0;right:0;top:140px;text-align:center;color:#fff;font-size:59px;line-height:64px;font-weight:700;letter-spacing:-.5px}

/* headings */
.sec-title{font-size:19px;font-weight:400;color:var(--heading);line-height:22px;border-left:4px solid var(--blue-mid);padding-left:12px;letter-spacing:.3px}
.sec-title.center{display:inline-block}
.center-wrap{text-align:center}
.lead{text-align:center;width:620px;margin:22px auto 0;font-size:11.5px}

.btn{display:inline-block;height:30px;line-height:30px;padding:0 12px;color:#fff;font-size:11px;font-weight:700;text-decoration:none;letter-spacing:.2px}
.btn-green{background:var(--green)}
.btn-blue{background:var(--blue-mid)}
.btn-orange{background:var(--orange)}
.btn-navy{background:var(--blue)}

.photo{position:absolute}

/* feature rows */
.advice{height:281px}
.advice .copy{position:absolute;left:0;top:42px;width:540px}
.advice .copy p{margin-top:16px}
.advice .actions{margin-top:14px;display:flex;gap:12px}
.advice .photo{left:586px;top:43px;width:292px;height:188px;background:linear-gradient(135deg,#9fb6cc,#d8dde3 50%,#5a7390)}

.looks{height:300px;background:var(--grey-band);border-top:1px solid #e4e4e4;border-bottom:1px solid #e4e4e4}
.looks .photo{left:0;top:52px;width:292px;height:187px;background:linear-gradient(135deg,#b9a48f,#e9e4de 45%,#3e434b)}
.looks .copy{position:absolute;left:335px;top:50px;width:543px}
.looks .copy p{margin-top:16px}
.looks .btn{margin-top:14px;background:var(--orange)}

/* essentials */
.essentials{height:423px}
.essentials .center-wrap{padding-top:42px}
.cards{position:absolute;left:0;top:151px;display:flex;gap:12px}
.card{width:284px;height:227px;color:#fff;text-align:center;padding:24px 22px 0}
.card svg{display:block;margin:0 auto}
.card h3{font-size:13px;font-weight:400;margin-top:24px}
.card p{font-size:10.5px;line-height:19px;margin-top:18px}
.card.green{background:var(--green)}
.card.blue{background:var(--blue-mid)}
.card.orange{background:var(--orange)}

/* further resources */
.further{height:477px;background:var(--grey-band);border-top:1px solid #e4e4e4}
.further .center-wrap{padding-top:40px}
.res-grid{position:absolute;left:0;top:137px;display:flex;gap:24px}
.res{width:201px}
.res .thumb{height:120px}
.res h4{font-size:13px;font-weight:400;color:var(--blue-mid);line-height:19px;margin-top:12px;height:40px}
.res p{font-size:10.5px;line-height:19px;margin-top:4px}
.res .btn{margin-top:12px;height:27px;line-height:27px;font-size:10px;padding:0 10px}

/* testimonials */
.testimonials{height:271px}
.testimonials .center-wrap{padding-top:52px}
.avatar{position:absolute;left:0;top:106px;width:113px;height:113px;border-radius:50%;background:linear-gradient(160deg,#d8cfc6,#a99b90)}
.quote-badge{position:absolute;left:80px;top:180px;width:38px;height:38px;border-radius:50%;background:var(--orange);border:3px solid #fff;color:#fff;font-size:24px;font-weight:700;text-align:center;line-height:40px}
.quote{position:absolute;left:137px;top:112px;width:741px;font-style:italic;font-size:11px;line-height:20px}
.quote .mark{color:var(--orange);font-weight:700;font-style:normal}
.quote cite{display:block;font-style:normal;font-size:10px;margin-top:12px;letter-spacing:.3px}

/* badges */
.badges{height:124px;border-top:1px solid #ddd}
.badge-row{position:absolute;left:0;top:18px;display:flex;align-items:center;gap:14px}
.seal{width:58px;height:58px;border-radius:50%;background:#c8a43c}
.partner{width:200px;height:44px;display:flex;align-items:center;font-size:17px;font-weight:700;color:var(--blue);line-height:18px}
.award{width:118px;height:66px;border-radius:50%;background:#e9e3cf}
.ribbon{width:150px;height:52px;background:var(--orange-deep)}
.roundel{width:68px;height:68px;border-radius:50%;background:var(--orange-deep)}

/* footer */
.site-footer{height:217px;background:var(--footer);color:#ddd}
.site-footer h5{font-size:14px;font-weight:400;color:#fff;letter-spacing:.5px}
.f-contact{position:absolute;left:0;top:40px}
.f-contact ul{list-style:none;margin-top:14px;font-size:10.5px;line-height:22px}
.f-contact li{display:flex;gap:10px;align-items:flex-start}
.f-contact li svg{margin-top:6px;flex:none}
.f-news{position:absolute;left:330px;top:40px}
.f-form{display:flex;margin-top:14px}
.f-input{width:212px;height:33px;background:#3a3a3a;color:#bbb;font-style:italic;font-size:10px;line-height:33px;padding-left:10px}
.f-submit{width:68px;height:33px;background:var(--green);color:#fff;font-weight:700;font-size:11px;line-height:33px;text-align:center}
.socials{display:flex;gap:8px;margin-top:16px}
.socials span{width:24px;height:24px;border:2px solid #ccc;border-radius:50%}
.f-brand{position:absolute;right:0;top:40px;color:#fff}
.f-brand .brand-name{font-size:40px;line-height:40px}
.f-brand .copy{font-size:10px;line-height:18px;margin-top:14px;color:#ddd}
</style>
</head>
<body>

<header class="site-header">
  <div class="wrap">
    <div class="brand">
      <div class="brand-name">brightfold</div>
      <div class="brand-tag">PROFESSIONAL SOLUTIONS</div>
      <div class="brand-sub">Résumés, CVs, Profiles &amp; Job Application Experts</div>
    </div>
    <div class="top-contact">
      <span><svg width="10" height="10" viewBox="0 0 10 10"><path d="M2 0l2 2.5-1.2 1.3a6 6 0 0 0 3.4 3.4L7.5 6 10 8 8.5 10C4 10 0 6 0 1.5z" fill="#fff"/></svg>061 555 0142</span>
      <span><svg width="11" height="8" viewBox="0 0 11 8"><rect width="11" height="8" fill="#fff"/><path d="M0 0l5.5 4.5L11 0" stroke="#0355a3" fill="none"/></svg>info@brightfoldsolutions.com</span>
    </div>
    <nav class="main-nav">
      <a href="#">HOME</a><a href="#">ABOUT</a><a href="#">RESUME SOLUTIONS</a><a href="#" class="active">CAREER RESOURCES</a><a href="#">PORTFOLIO</a><a href="#">CONTACT US</a>
    </nav>
  </div>
</header>

<section class="hero" role="img" aria-label="Photo of two businessmen in discussion across a desk with a computer">
  <h1>CAREER RESOURCES<br>ON BRIGHTFOLD SOLUTIONS</h1>
</section>

<section class="advice">
  <div class="wrap">
    <div class="copy">
      <h2 class="sec-title">CAREER ADVICE &amp; EMPLOYMENT TREND FOR 2016</h2>
      <p>As we move into an Employers Driven Market, planning the right strategy can be critical to seeking success. The Hidden Job Market can be an extremely useful ally in understanding what's beneath the surface. Lorem ipsum dolor sit amet, consectetur adipiscing elit, sed do eiusmod tempor incididunt ut labore et dolore magna aliqua. Ut enim ad minim veniam, quis nostrud exercitation ullamco laboris nisi ut aliquip ex ea commodo consequat. Duis aute irure dolor in reprehenderit in voluptate velit esse cillum dolore eu fugiat nulla pariatura commodo consequat. Duis aute irure dolor in reprehenderit in voluptate velit esse cillum dolore.</p>
      <div class="actions"><a class="btn btn-green" href="#">THE HIDDEN JOB MARKET</a><a class="btn btn-blue" href="#">FIND OUT MORE HERE</a></div>
    </div>
    <div class="photo" role="img" aria-label="Photo of a businesswoman writing at an office desk"></div>
  </div>
</section>

<section class="looks">
  <div class="wrap">
    <div class="photo" role="img" aria-label="Photo of a smiling woman in a job interview"></div>
    <div class="copy">
      <h2 class="sec-title">HOW FAR WILL LOOKS GET YOU?</h2>
      <p>Are you Australia's next top model or just your average Joe? How far do employers judge a book by its cover? Here we look at a few simple measures that can make a world of difference sed do eiusmod tempor incididunt ut labore et dolore magna aliqua. Ut enim ad minim veniam, quis nostrud exercitation ullamco laboris nisi ut aliquip ex ea commodo consequat. Duis aute irure dolor in reprehenderit in voluptate velit esse cillum dolore eu fugiat nulla pariatura commodo consequat. Duis aute irure dolor in reprehenderit in voluptate velit esse cillum dolouis aute irure dolor in reprehenderit in voluptate velit.</p>
      <a class="btn" href="#">SIMPLE DRESS SENSE CAN MAKE A WORLD OF DIFFERENCE</a>
    </div>
  </div>
</section>

<section class="essentials">
  <div class="wrap">
    <div class="center-wrap"><h2 class="sec-title center">CAREER ESSENTIALS</h2></div>
    <p class="lead">Before you even begin your employment search, there are a few basic rules to follow:- Suis aute irure dolor in reprehenderit in voluptate velit esse cillum dolore eu fugiat nulla pariatura commodo consequat. Duis aute irure dolor in reprehenderit in voluptate velit esse cillum doloruis aute irure dolor in reprehenderit in voluptate velit.</p>
    <div class="cards">
      <div class="card green">
        <svg width="48" height="44" viewBox="0 0 48 44"><circle cx="24" cy="9" r="8" fill="#fff"/><path d="M10 34c0-9 6-15 14-15s14 6 14 15z" fill="#fff"/><rect x="4" y="34" width="40" height="5" fill="#fff"/></svg>
        <h3>Preparation is critical</h3>
        <p>Recruitment agencies - are they friends or foe? Whether you like them or not, you'll need to learn some basic principles to avoid being "blacklisted"</p>
      </div>
      <div class="card blue">
        <svg width="56" height="44" viewBox="0 0 56 44"><circle cx="28" cy="10" r="8" fill="#fff"/><circle cx="11" cy="16" r="6" fill="#fff"/><circle cx="45" cy="16" r="6" fill="#fff"/><path d="M14 42c0-11 6-18 14-18s14 7 14 18z" fill="#fff"/><path d="M0 40c0-8 4-14 11-14 3 0 5 1 6 2-3 3-5 7-5 12z" fill="#fff"/><path d="M56 40c0-8-4-14-11-14-3 0-5 1-6 2 3 3 5 7 5 12z" fill="#fff"/></svg>
        <h3>Working with Recruitment Agencies</h3>
        <p>Not sure what money you should be asking for? Here's a rundown on just how to approach salary advice</p>
      </div>
      <div class="card orange">
        <svg width="48" height="44" viewBox="0 0 48 44"><ellipse cx="30" cy="6" rx="12" ry="4" fill="#fff"/><ellipse cx="30" cy="13" rx="12" ry="4" fill="#fff"/><ellipse cx="30" cy="20" rx="12" ry="4" fill="#fff"/><path d="M2 32h10l8 3h12c3 0 3 4 0 4H18l14 2 14-8c3-1 4 2 1 4L32 44H2z" fill="#fff"/></svg>
        <h3>Salary advice here</h3>
        <p>Sed ut perspiciatis unde omnis iste natus error sit voluptatem accusantium doloremque laudantium, totam rem aperiam, eaqu.</p>
      </div>
    </div>
  </div>
</section>

<section class="further">
  <div class="wrap">
    <div class="center-wrap"><h2 class="sec-title center">FURTHER CAREER RESOURCES</h2></div>
    <p class="lead" style="width:580px;margin-top:18px">Just how important is it to understand the differences in the market today ?- Suis aute irure dolor in reprehenderit in voluptate velit esse cillum dolore eu fugiat nulla pariatura commodo consequat. Duis aute irure dolor in reprehenderit.</p>
    <div class="res-grid">
      <div class="res">
        <div class="thumb" role="img" aria-label="Photo of an interview panel at a table" style="background:linear-gradient(135deg,#8c8f96,#d7d3cf 50%,#30343b)"></div>
        <h4>A look into an employers<br>driven market</h4>
        <p>We are currently at an important time in the job market, a time which is regarded as a seasonal high. Employment advertising is growing fast.</p>
        <a class="btn btn-orange" href="#">READ MORE</a>
      </div>
      <div class="res">
        <div class="thumb" role="img" aria-label="Photo of a woman with curly hair in an office" style="background:linear-gradient(135deg,#a88f6e,#e6dccd 50%,#5a4a3c)"></div>
        <h4>Changing careers,<br>career advice here</h4>
        <p>We are currently at an important time in the job market, a time which is regarded as a seasonal high. Employment advertising is growing fast.</p>
        <a class="btn btn-navy" href="#">READ MORE</a>
      </div>
      <div class="res">
        <div class="thumb" role="img" aria-label="Photo of a woman speaking with colleagues in a meeting" style="background:linear-gradient(135deg,#c5c1bb,#f0eeea 50%,#3f3a36)"></div>
        <h4>Age awareness career<br>advice here</h4>
        <p>We are currently at an important time in the job market, a time which is regarded as a seasonal high. Employment advertising is growing fast.</p>
        <a class="btn btn-navy" href="#">READ MORE</a>
      </div>
      <div class="res">
        <div class="thumb" role="img" aria-label="Photo of a business handshake across a desk" style="background:linear-gradient(135deg,#7d8fa6,#dfe4ea 50%,#3b4656)"></div>
        <h4>Resume templates and software</h4>
        <p>We are currently at an important time in the job market, a time which is regarded as a seasonal high. Employment advertising is growing fast.</p>
        <a class="btn btn-navy" href="#">READ MORE</a>
      </div>
    </div>
  </div>
</section>

<section class="testimonials">
  <div class="wrap">
    <div class="center-wrap"><h2 class="sec-title center">CLIENT TESTIMONIALS</h2></div>
    <div class="avatar" role="img" aria-label="Portrait photo of the client"></div>
    <div class="quote-badge">&ldquo;</div>
    <blockquote class="quote">
      <span class="mark">&ldquo;</span> At vero eos et accusamus et iusto odio dignissimos ducimus qui blanditiis praesentium voluptatum deleniti atque corrupti quos dolores et quas mol estias excepturi sint occaecati cupiditate non provident, similique sunt in culpa qui officia deserunt mollitia animi, id est laborum et dolorum fuga. Et harum quidem rerum facilis est et expedita distinctio. Nam libero tempore, cum soluta nobis est eligendi optio cumque nihil impedit quo minus id quod maxime placeat facere uidem rerum facilis est et expedita distinctioam libero <span class="mark">&rdquo;</span>
      <cite>JANA HOLT, CITY NAME</cite>
    </blockquote>
  </div>
</section>

<section class="badges">
  <div class="wrap">
    <div class="badge-row">
      <div class="seal"></div><div class="seal"></div><div class="seal"></div><div class="seal"></div>
      <div class="partner">Pathway Career Network</div>
      <div class="award"></div>
      <div class="ribbon"></div>
      <div class="roundel"></div>
    </div>
  </div>
</section>

<footer class="site-footer">
  <div class="wrap">
    <div class="f-contact">
      <h5>CONTACT US</h5>
      <ul>
        <li><svg width="10" height="9" viewBox="0 0 10 9"><path d="M5 0l5 4.5H8.5V9h-2.5V6h-2v3H1.5V4.5H0z" fill="#ddd"/></svg><span>Contact Us Send Me a Message / &nbsp;Contact Info<br>Address full Address goes here, cityname, country</span></li>
        <li><svg width="8" height="10" viewBox="0 0 8 10"><rect width="8" height="10" rx="1" fill="#ddd"/></svg><span>Phone : (415) 555-0178</span></li>
        <li><svg width="10" height="8" viewBox="0 0 10 8"><rect width="10" height="8" fill="#ddd"/><path d="M0 0l5 4 5-4" stroke="#262626" fill="none"/></svg><span>Email: name@example.com</span></li>
        <li><svg width="10" height="9" viewBox="0 0 10 9"><rect y="3" width="10" height="6" fill="#ddd"/><rect x="2" width="6" height="3" fill="#ddd"/></svg><span>Fax:-1-212-555-0130</span></li>
      </ul>
    </div>
    <div class="f-news">
      <h5>SUBSCRIBE NEWSLETTER</h5>
      <div class="f-form"><div class="f-input">Email Address:</div><div class="f-submit">SUBMIT</div></div>
      <div class="socials"><span></span><span></span><span></span><span></span></div>
    </div>
    <div class="f-brand">
      <div class="brand-name">brightfold</div>
      <div class="brand-tag">PROFESSIONAL SOLUTIONS</div>
      <div class="brand-sub">Résumés, CVs, Profiles &amp; Job Application Experts</div>
      <div class="copy">Copyright © 2016 &nbsp;All Rights Reserved.<br>brightfold Professional Solutions.</div>
    </div>
  </div>
</footer>

</body>
</html>
```